Business card for Mortgage broker business

I have already had the logo designed and am needing a great looking business card. My business focus is on servicing clients who may not be able to obtain finance through traditional lenders due to bad credit, short term employment or they just don't fit the banks profile. It needs to be professional, trust worthy but also have a caring fell about it.
I have provided files showing the green and black logo, the white logo(on white background so the file looks blank) and also a file with the white logo with a background of leaves that was made up which will probably be used for a website header.

Industry/Entity Type

Finance

Contact Information for Business Card

Marcus Dalby
Managing Director, Accredited Finance Broker(AFB)
Po Box 817, Pakenham VIC 3810
marcus@kestrelfunding.com.au
www.kestrelfunding.com.au
0438 216 507

Requirements
Nice to have
• I have added a picture of myself as I would like to see some designs with the pic in it, but I'm not sure if I want it on there with the logo's or just the logo's

```html
<!DOCTYPE html>
<html lang="en">
<head>
<meta charset="utf-8">
<title>Kestrel Funding – Business Card</title>
<link rel="stylesheet" href="https://fonts.googleapis.com/css2?family=Open+Sans:wght@400;600;700&display=swap">
<style>
  :root {
    --brand-green: #076a39;
    --card-white: #ffffff;
    --stage-bg: #e9ebea;
    --text-on-green: #ffffff;
  }
  * { margin: 0; padding: 0; box-sizing: border-box; }
  html, body {
    width: 1200px; height: 900px; overflow: hidden;
    background: var(--stage-bg);
    font-family: "Open Sans", Arial, sans-serif;
  }
  .canvas { position: relative; width: 1200px; height: 900px; }

  .card {
    position: absolute;
    box-shadow: 0 6px 18px rgba(0,0,0,0.12);
    overflow: hidden;
  }

  /* Front card */
  .card-front {
    left: 238px; top: 62px; width: 555px; height: 343px;
    background: var(--brand-green);
    color: var(--text-on-green);
  }
  .card-front .dove-area {
    position: absolute; left: 265px; top: 0; width: 290px; height: 343px;
  }
  .holder { position: absolute; left: 42px; top: 33px; }
  .holder-name { font-size: 18px; font-weight: 700; line-height: 23px; }
  .holder-title { font-size: 14px; font-weight: 400; line-height: 18px; }

  .contact-list {
    position: absolute; left: 42px; top: 170px;
    list-style: none; font-size: 14.5px; line-height: 20.5px;
  }
  .contact-list li { display: flex; align-items: center; gap: 8px; }
  .contact-list svg { width: 11px; height: 11px; fill: var(--text-on-green); }
  .address {
    position: absolute; left: 42px; top: 267px;
    font-size: 14.5px; line-height: 20px; font-style: normal;
  }

  /* Back card */
  .card-back {
    left: 457px; top: 519px; width: 558px; height: 342px;
    background: var(--card-white);
  }
  .brand-mark {
    position: absolute; left: 0; right: 0; top: 116px;
    display: flex; justify-content: center; align-items: center; gap: 14px;
  }
  .brand-dot {
    width: 22px; height: 22px; border-radius: 50%;
    background: var(--brand-green);
  }
  .brand-name {
    font-size: 40px; font-weight: 600; color: var(--brand-green);
    line-height: 52px; letter-spacing: 0.5px;
  }
  .back-website {
    position: absolute; left: 0; right: 0; top: 267px;
    text-align: center; font-size: 15px; letter-spacing: 2.6px;
    line-height: 20px; color: var(--brand-green); font-weight: 600;
  }
</style>
</head>
<body>
<main class="canvas">

  <section class="card card-front" aria-label="Business card front">
    <svg class="dove-area" viewBox="0 0 290 343" role="img" aria-label="Large dove carrying an olive branch illustration">
      <defs>
        <linearGradient id="doveFill" x1="0" y1="0" x2="1" y2="1">
          <stop offset="0" stop-color="#ffffff"/>
          <stop offset="1" stop-color="#eef3ef"/>
        </linearGradient>
      </defs>
      <path d="M7 0 H290 V343 H150 C130 310 118 260 110 230 C100 200 92 170 82 140 C70 110 60 90 55 60 C45 35 25 15 7 0 Z" fill="url(#doveFill)"/>
    </svg>

    <div class="holder">
      <p class="holder-name">Jonathan Smith</p>
      <p class="holder-title">Managing Director</p>
    </div>

    <ul class="contact-list">
      <li>
        <svg viewBox="0 0 24 24" aria-hidden="true"><path d="M6.6 10.8a15.1 15.1 0 0 0 6.6 6.6l2.2-2.2a1 1 0 0 1 1-.25 11.4 11.4 0 0 0 3.6.57 1 1 0 0 1 1 1V20a1 1 0 0 1-1 1A17 17 0 0 1 3 4a1 1 0 0 1 1-1h3.5a1 1 0 0 1 1 1c0 1.25.2 2.45.57 3.6a1 1 0 0 1-.25 1z"/></svg>
        <span>044-123 456 789</span>
      </li>
      <li>
        <svg viewBox="0 0 24 24" aria-hidden="true"><path d="M6 2h9v5h3a2 2 0 0 1 2 2v11a2 2 0 0 1-2 2H6a2 2 0 0 1-2-2V4a2 2 0 0 1 2-2zm2 2v5h5V4zm1 9v2h2v-2zm4 0v2h2v-2zm-4 4v2h2v-2zm4 0v2h2v-2z"/></svg>
        <span>044-123 456 789</span>
      </li>
      <li>
        <svg viewBox="0 0 24 24" aria-hidden="true"><path d="M2 5h20v14H2zm2 2v.5l8 5 8-5V7z"/></svg>
        <span>info@webname.com</span>
      </li>
      <li><span>www.websitename.com</span></li>
    </ul>

    <address class="address">
      12345, Address Goes Here<br>
      Country Name, 123456.
    </address>
  </section>

  <section class="card card-back" aria-label="Business card back">
    <div class="brand-mark">
      <span class="brand-name">Kestrel Funding</span>
      <span class="brand-dot" aria-hidden="true"></span>
    </div>
    <p class="back-website">www.websitename.com</p>
  </section>

</main>
</body>
</html>
```